Site for company producing and selling products for children's health

We need an appealing professional web site design and images for a brand new company producing and selling products focused on children’s health. The site will offer information to visitors on the company, the company’s products, and general resources related to children’s health. Additionally the site will offer e-commerce functionality to allow for ordering of the company’s products.
The content and navigation for the site will be generated by programming, such as php or asp, and therefore any images used in the navigation portions of the site should allow for HTML markup to be overlaid rather than having the text built into the image or graphic.
The design must include 2 layouts, one for the landing/home page that includes only top navigation, and an inner page layout that includes both top and left navigation.
The header area of the site should include a place for links to access the visitor’s cart and profile similar to the top sections of plumvat.com, tidelor.com, and keenmart.com.
The landing page of the site should include some type of “changing” image area where we can include multiple image files for rotation to visitors similar to what is seen at vorta.com or brisksip.com. The flash/animation mechanism does not need to be provided (although it would be a plus if it was) but the design must accommodate the space for it.
The company’s colors are Orange (FF9900) and Blue (0066FF) and the logo can be viewed at http://wonkibrook.com/logo.png
All CSS and markup provided must be display consistently in Internet Explorer 7+, FifeFox, Google Chrome, and Safari.
Incorporating social media links (facebook, twitter, etc.) is desirable.
Parents who are conscious of health risks associated with children's diets and consumer food products.
E-Commerce

```html
<!DOCTYPE html>
<html lang="en">
<head>
<meta charset="utf-8">
<title>Wonkibrook – Healthy Products for Kids</title>
<link rel="stylesheet" href="https://fonts.googleapis.com/css2?family=Arimo:wght@400;700&family=PT+Sans:wght@400;700&family=Oswald:wght@500;600&family=Open+Sans:wght@600;700&display=swap">
<style>
  :root {
    --orange: #ff9900;
    --orange-deep: #e86a00;
    --orange-nav: #ee7a08;
    --blue: #0066ff;
    --sky: #4aa3e6;
    --sky-light: #5db6ee;
    --ink: #222;
    --grey-text: #444;
    --rule: #b9b9b9;
    --panel-line: #d6dce6;
    --ad-grey: #e6e6e6;
    --red: #ff1a00;
    --navy-btn: #0a3fd6;
  }
  * { box-sizing: border-box; margin: 0; padding: 0; }
  html, body { width: 1091px; height: 1200px; overflow: hidden; }
  body {
    background: linear-gradient(180deg, #e9eef8 0%, #f4f6fb 30%, #fafbfd 100%);
    font-family: Arimo, Arial, sans-serif;
    color: var(--ink);
  }
  .page {
    position: relative; width: 1002px; height: 1100px;
    transform: scale(1.0888); transform-origin: 0 0;
  }
  .abs { position: absolute; }

  /* header */
  .brand { left: 27px; top: 40px; display: flex; align-items: center; gap: 8px; }
  .brand-dot { width: 22px; height: 22px; border-radius: 50%; background: var(--orange); }
  .brand-name { font: 700 28px Arimo, Arial, sans-serif; color: var(--blue); letter-spacing: -0.5px; }
  .utility { right: 20px; top: 61px; font-size: 11px; color: #111; word-spacing: 1px; }
  .utility span { margin: 0 8px; }
  .currency {
    left: 733px; top: 81px; width: 114px; height: 19px; background: #fff;
    border: 1px solid #8a9ab3; font-size: 11px; padding: 2px 4px; color: #111;
  }
  .currency::after {
    content: ""; position: absolute; right: 1px; top: 1px; width: 15px; height: 15px;
    background: linear-gradient(#dde7f7, #b8c9e6);
  }
  .cart { left: 868px; top: 84px; font-size: 11px; font-weight: 700; letter-spacing: .5px; display: flex; gap: 6px; align-items: center; }

  /* navigation */
  .nav {
    left: 20px; top: 112px; width: 962px; height: 34px;
    background: linear-gradient(180deg, #f6922a 0%, var(--orange-nav) 50%, #d95f00 100%);
    display: flex; align-items: center;
  }
  .nav a {
    color: #fff; text-decoration: none; font-size: 13px; font-weight: 700;
    height: 100%; display: flex; align-items: center; justify-content: center;
    border-right: 1px solid rgba(255,255,255,.35);
  }
  .nav a.current { background: linear-gradient(180deg, #e0610a, #b84800); width: 113px; position: relative; }
  .nav a.current::before {
    content: ""; position: absolute; top: 0; left: 50%; margin-left: -5px;
    border: 5px solid transparent; border-top-color: #fff;
  }
  .search { position: absolute; left: 742px; top: 7px; display: flex; align-items: center; gap: 10px; }
  .search input {
    width: 145px; height: 21px; border: 1px solid #ccc; font: 11px Arimo, Arial, sans-serif; padding: 0 4px;
  }
  .search .go { width: 36px; height: 21px; background: #111; color: #fff; font-size: 11px; font-weight: 700; display: flex; align-items: center; justify-content: center; }

  /* hero */
  .hero-frame { left: 19px; top: 154px; width: 759px; height: 314px; background: #fff; border: 1px solid #e1e4ea; }
  .hero-photo {
    position: absolute; left: 10px; top: 10px; width: 738px; height: 293px;
    background: linear-gradient(100deg, #8fbf7a 0%, #e9c9a7 30%, #f2d6c0 55%, #cfe3f2 80%, #e9f2fa 100%);
  }
  .hero-copy { position: absolute; left: 507px; top: 22px; }
  .hero-copy h2 { font: 400 21px/22px "PT Sans", Arial, sans-serif; color: #111; text-transform: uppercase; }
  .hero-copy p { font-size: 11px; margin-top: 6px; margin-left: 5px; }

  /* content */
  .welcome { left: 21px; top: 483px; font: 400 28px Arimo, Arial, sans-serif; color: #333; letter-spacing: -.8px; transform: scaleX(.93); transform-origin: left; }
  .welcome em { font-style: normal; color: var(--blue); }
  .rule { left: 20px; width: 756px; border-top: 1px dashed var(--rule); }
  .intro { left: 19px; top: 540px; width: 758px; font-size: 11px; line-height: 18px; text-align: justify; color: #111; }
  .section-title { left: 20px; top: 647px; font-size: 18px; color: var(--blue); }

  .product { width: 182px; top: 705px; }
  .product .thumb { height: 149px; border: 1px solid #c9c9c9; background: #f2f2f2; padding: 6px; }
  .product .thumb div { width: 100%; height: 100%; }
  .product .caption { margin-top: 14px; font: 700 11.5px "Open Sans", Verdana, sans-serif; letter-spacing: .4px; }

  .ads {
    left: 20px; top: 907px; width: 756px; height: 96px; background: var(--ad-grey);
    display: flex; align-items: center; justify-content: center;
    font: 700 24px "Open Sans", Verdana, sans-serif; color: #333; letter-spacing: 1px;
  }

  /* sidebar */
  .side-box { left: 787px; width: 195px; background: #fff; border: 1px solid var(--panel-line); padding: 4px; }
  .side-inner { height: 100%; }
  .signin .side-inner { background: var(--sky); padding: 8px 7px; color: #111; }
  .side-head { font: 400 22px "PT Sans", Arial, sans-serif; color: #fff; letter-spacing: .5px; }
  .field { display: block; width: 171px; height: 22px; background: #fff; border: 1px solid #ccc; font-size: 11px; padding: 4px 5px; margin-top: 8px; }
  .btn-orange { display: inline-block; background: var(--orange); border: 1px solid #fff; color: #fff; font-size: 11px; font-weight: 700; padding: 4px 6px; }
  .forgot { font-size: 11px; margin-top: 10px; }
  .forgot b { color: #000; }
  .newcomer { color: #fff; font-size: 11px; font-weight: 700; line-height: 17px; margin: 13px 0 0 5px; }
  .newcomer .free { color: var(--red); }
  .signup {
    margin-top: 12px; height: 47px; background: linear-gradient(180deg, #2c7df0, var(--navy-btn));
    color: #fff; font: 700 26px "PT Sans", Arial, sans-serif; display: flex; align-items: center; justify-content: center; letter-spacing: .5px;
  }
  .catalog .side-inner {
    background: linear-gradient(180deg, var(--orange), var(--orange-deep));
    display: flex; align-items: center; gap: 6px; padding: 0 6px;
  }
  .catalog .folder { width: 48px; height: 54px; border-radius: 4px; background: linear-gradient(#ffd64a, #f4a40a); flex: none; }
  .catalog p { font: 600 22px/24px Oswald, "Arial Narrow", sans-serif; color: #fff; letter-spacing: .3px; }
  .catalog p span { color: var(--red); }
  .newsletter .side-inner { background: linear-gradient(180deg, var(--sky), var(--sky-light)); padding: 8px 9px; }
  .newsletter p { font-size: 11px; font-weight: 700; line-height: 16px; margin-top: 6px; color: #111; }
  .newsletter .field { width: 170px; margin-top: 17px; }
  .order .side-inner { background: linear-gradient(180deg, #f7a000, #ee7c00); padding: 10px 6px; color: #fff; }
  .order h4 { font: 600 19px Oswald, "Arial Narrow", sans-serif; letter-spacing: -.2px; }
  .order .phones { font: 600 17px/23px Oswald, "Arial Narrow", sans-serif; color: #111; margin-top: 6px; }

  /* footer */
  .footer { left: 20px; top: 1019px; width: 962px; height: 75px; background: var(--orange); color: #fff; font-size: 11px; padding: 16px 11px; }
  .footer span { margin: 0 7px; }
  .footer p + p { margin-top: 4px; }
</style>
</head>
<body>
<div class="page">

  <header>
    <div class="abs brand"><div class="brand-dot"></div><div class="brand-name">wonkibrook</div></div>
    <div class="abs utility">SHIPPING<span>|</span>MY ACCOUNT<span>|</span>ORDER TRACKING</div>
    <div class="abs currency">Select Currency</div>
    <div class="abs cart">
      <svg width="14" height="12" viewBox="0 0 14 12"><path d="M0 1h3l2 7h7l2-5H4" fill="none" stroke="#f07800" stroke-width="1.6"/><circle cx="6" cy="10.5" r="1.3" fill="#f07800"/><circle cx="11" cy="10.5" r="1.3" fill="#f07800"/></svg>
      <span>CART &nbsp;0 &nbsp;ITEMS</span>
    </div>
  </header>

  <nav class="abs nav">
    <a class="current" href="#">Home</a>
    <a href="#" style="width:113px">About Us</a>
    <a href="#" style="width:122px">Products</a>
    <a href="#" style="width:124px">Services</a>
    <a href="#" style="width:103px">News</a>
    <a href="#" style="width:135px;border-right:0">Contact Us</a>
    <div class="search">
      <svg width="20" height="20" viewBox="0 0 20 20"><circle cx="12" cy="8" r="5.5" fill="none" stroke="#fff" stroke-width="2"/><path d="M8 12l-6 6" stroke="#fff" stroke-width="2.6" stroke-linecap="round"/></svg>
      <input type="text" value="Enter Keyword">
      <div class="go">GO</div>
    </div>
  </nav>

  <section class="abs hero-frame">
    <div class="hero-photo" role="img" aria-label="Rotating banner: a smiling family of four seated together outdoors"></div>
    <div class="hero-copy">
      <h2>Are you worried<br>about your kid’s<br>health?</h2>
      <p>Lorem ipsum dolor site amet</p>
    </div>
  </section>

  <h1 class="abs welcome">welcome to <em>Wonkibrook</em></h1>
  <div class="abs rule" style="top:524px"></div>
  <p class="abs intro">Lorem ipsum dolor sit amet, consectetur adipiscing elit. Ut aliquet lacus et dolor mollis bibendum. Mauris sodales magna vel erat porttitor vel hendrerit velit lacinia. Vestibulum neque libero, placerat eget sagittis vel, vulputate eget lectus. Nullam tortor libero, dapibus tempus elementum id, feugiat vel odio. Proin in orci quis ipsum hendrerit mattis. Nullam lectus odio, venenatis at laoreet non, consectetur id massa. Vestibulum tempor porta volutpat. Nunc quis velit sem, et euismod nunc. Maecenas arcu tellus, viverra in scelerisque id, tristique eu massa. Curabitur scelerisque, urna suscipit interdum pretium, tortor nisl adipiscing lorem, quis pharetra metus orci at elit.</p>

  <h2 class="abs section-title">Products</h2>
  <div class="abs rule" style="top:684px"></div>

  <article class="abs product" style="left:19px">
    <div class="thumb"><div role="img" aria-label="Fresh fruit: oranges, pears and grapes" style="background:linear-gradient(135deg,#f08a1a,#d9c23a 55%,#b82a1e)"></div></div>
    <p class="caption">Lorem Ipsum Dolor Sit Amt</p>
  </article>
  <article class="abs product" style="left:212px">
    <div class="thumb"><div role="img" aria-label="Vegetable wrap with tomatoes and lettuce" style="background:linear-gradient(135deg,#c23a2a,#e8d4b4 50%,#6d9a3a)"></div></div>
    <p class="caption">Lorem Ipsum Dolor Sit Amt</p>
  </article>
  <article class="abs product" style="left:404px">
    <div class="thumb"><div role="img" aria-label="Chocolate ice cream sundae with a cherry" style="background:radial-gradient(circle at 50% 55%,#6a3a22 0%,#8a5236 30%,#fff 60%)"></div></div>
    <p class="caption">Lorem Ipsum Dolor Sit Amt</p>
  </article>
  <article class="abs product" style="left:597px">
    <div class="thumb"><div role="img" aria-label="Orange, cherries, lime and pineapple" style="background:linear-gradient(135deg,#f2901c,#d86a12 45%,#c21f1f 80%,#7fa83a)"></div></div>
    <p class="caption">Lorem Ipsum Dolor Sit Amt</p>
  </article>

  <div class="abs ads">Advertisements</div>

  <aside>
    <div class="abs side-box signin" style="top:154px;height:271px">
      <div class="side-inner">
        <h3 class="side-head">SIGN IN</h3>
        <div class="field" style="margin-top:5px">userid</div>
        <div class="field" style="margin-top:11px">password</div>
        <div style="margin-top:10px"><span class="btn-orange">Sign In</span></div>
        <p class="forgot">Forgot your password ?<b>Click Here</b></p>
        <p class="newcomer">Are You NEW? Register yourself.It is Totally <span class="free">FREE</span></p>
        <div class="signup">SIGN UP</div>
      </div>
    </div>

    <div class="abs side-box catalog" style="top:431px;height:96px">
      <div class="side-inner">
        <div class="folder" role="img" aria-label="Folder holding catalog pages"></div>
        <p>ORDER OUR<br><span>FREE</span> CATALOG</p>
      </div>
    </div>

    <div class="abs side-box newsletter" style="top:537px;height:208px">
      <div class="side-inner">
        <h3 class="side-head">NEWSLETTER</h3>
        <p>To get special coupons and Special Offer subscribe our newsletter. You can any time UNSUBSCRIBE .</p>
        <div class="field">your email id</div>
        <div style="margin-top:14px"><span class="btn-orange">Submit</span></div>
      </div>
    </div>

    <div class="abs side-box order" style="top:759px;height:244px">
      <div class="side-inner">
        <h4>ORDER US</h4>
        <p class="phones">(800) 555 - 0141<br>(800) 555 - 0143</p>
        <h4 style="margin-top:50px">CUSTOMER SERVICE</h4>
        <p class="phones">(800) 555 - 0172<br>(800) 555 - 0172</p>
      </div>
    </div>
  </aside>

  <footer class="abs footer">
    <p>Home<span>|</span>About Us<span>|</span>Product<span>|</span>Services<span>|</span>News<span>|</span>My Account<span>|</span>Sitemap<span>|</span>FAQ<span>|</span>Customer Service<span>|</span>Contact Us</p>
    <p>© 2010, Wonkibrook. All rights reserved. Privacy Policy<span>|</span>Terms &amp; Conditions</p>
  </footer>

</div>
</body>
</html>
```